Business Card Design Project

We need a business card design for a relatively new company called Velmar Gear. We design paddle (an outdoor winter sport primarily played in the midwest and east coast) and tennis bags for women and men. Velmar Gear is a lifestyle brand for the next generation country club goers. Our bags merge fashion with functionality and are making country club sports trendier and more fashionable.

I would like to include space for
Name: (will fill this in for employees)
Velmar Gear
Phone: (will do this)
Email:
www.velmargear.example

Would also like to include Chatterbook and Flitter icons.
Please do not use pictures of the bags - this is just to give you an idea of what style bags we sell.

Target Market(s)

30 to 40 year old men and women - luxury market

Industry/Entity Type

Fashion

Requirements
Must have
• Would like the company logo included

```html
<!DOCTYPE html>
<html lang="en">
<head>
<meta charset="utf-8">
<title>Velmar Gear – Business Card</title>
<link href="https://fonts.googleapis.com/css2?family=Questrial&display=swap" rel="stylesheet">
<style>
  :root {
    --stage: #2e2e2e;
    --card-back-light: #d4d4d4;
    --card-back-dark: #c2c2c2;
    --ink-dark: #231f20;
    --ink-mid: #3a3a3a;
    --orange: #f7822a;
    --orange-deep: #ef6a1f;
    --white: #ffffff;
  }
  * { box-sizing: border-box; margin: 0; padding: 0; }
  html, body { width: 1200px; height: 900px; overflow: hidden; }
  body {
    background: var(--stage);
    font-family: "Questrial", "Century Gothic", sans-serif;
    position: relative;
  }
  .card {
    position: absolute;
    top: 301px;
    width: 513px;
    height: 296px;
    border-radius: 18px;
    overflow: hidden;
  }
  /* Back side */
  .card--back {
    left: 73px;
    background: linear-gradient(160deg, var(--card-back-light), var(--card-back-dark));
  }
  .card--back .brand-mark {
    position: absolute;
    left: 0; right: 0; top: 96px;
    display: flex; align-items: center; justify-content: center; gap: 14px;
    color: var(--ink-dark);
    font-size: 40px;
  }
  .brand-mark .dot {
    width: 26px; height: 26px; border-radius: 50%;
    background: var(--ink-dark);
  }
  .card--back .website {
    position: absolute;
    left: 0; right: 0; top: 258px;
    text-align: center;
    font-size: 14px;
    color: var(--ink-mid);
  }
  /* Front side */
  .card--front {
    left: 616px;
    background: var(--orange);
  }
  .front-decoration {
    position: absolute;
    left: 318px; top: 70px;
    width: 240px; height: 240px;
    border-radius: 50%;
    background: var(--orange-deep);
  }
  .front-header {
    position: absolute;
    left: 28px; top: 26px;
    display: flex; align-items: center; gap: 16px;
    color: var(--white);
    font-size: 48px;
    line-height: 1;
  }
  .front-header .dot {
    width: 36px; height: 36px; border-radius: 50%;
    border: 5px solid var(--white);
  }
  .person {
    position: absolute;
    left: 44px; top: 170px;
    color: var(--white);
  }
  .person-name { font-size: 29px; line-height: 1.1; }
  .person-role { font-size: 14px; margin-top: 2px; }
  .contacts {
    position: absolute;
    left: 44px; top: 242px;
    display: flex;
    color: var(--white);
    font-size: 14px;
    line-height: 18px;
  }
  .contact-list { list-style: none; padding-right: 12px; }
  .contact-list li { display: flex; align-items: center; gap: 5px; }
  .contact-list svg { width: 11px; height: 11px; fill: var(--white); }
  .social-list {
    list-style: none;
    border-left: 1px solid var(--white);
    padding-left: 12px;
  }
  .social-list li { display: flex; align-items: center; gap: 5px; }
  .social-list .square { width: 10px; height: 10px; background: var(--white); border-radius: 1px; }
</style>
</head>
<body>
  <section class="card card--back" aria-label="Card back">
    <div class="brand-mark"><span class="dot"></span><span>Velmar Gear</span></div>
    <p class="website">www.velmargear.example</p>
  </section>

  <section class="card card--front" aria-label="Card front">
    <div class="front-decoration"></div>
    <header class="front-header"><span class="dot"></span><span>Velmar Gear</span></header>
    <div class="person">
      <p class="person-name">Dorian Kessler</p>
      <p class="person-role">managing director</p>
    </div>
    <div class="contacts">
      <ul class="contact-list">
        <li>
          <svg viewBox="0 0 24 24" aria-hidden="true"><path d="M6.6 10.8a15.1 15.1 0 0 0 6.6 6.6l2.2-2.2a1 1 0 0 1 1-.25 11.4 11.4 0 0 0 3.6.57 1 1 0 0 1 1 1V20a1 1 0 0 1-1 1A17 17 0 0 1 3 4a1 1 0 0 1 1-1h3.5a1 1 0 0 1 1 1c0 1.25.2 2.45.57 3.57a1 1 0 0 1-.25 1z"/></svg>
          <span>555 014 27 36</span>
        </li>
        <li>
          <svg viewBox="0 0 24 24" aria-hidden="true"><path d="M2 5h20v14H2z M2 5l10 8 10-8" fill="var(--white)"/><path d="M3 6l9 7 9-7" fill="none" stroke="var(--orange)" stroke-width="2"/></svg>
          <span>info@velmargear.example</span>
        </li>
      </ul>
      <ul class="social-list">
        <li><span class="square"></span><span>VelmarGear</span></li>
        <li><span class="square"></span><span>VelmarGear1</span></li>
      </ul>
    </div>
  </section>
</body>
</html>
```